a Label for a candle jar and its gift box

I would like a label that is modern minimalist for candles jars. These jars are colored as white, amber and black. I am thinking maybe foiling gold/silver background with logo only and maybe company name in different color that suits the foiling background color/s. I would like a high quality luxurious design that shows the preciousness of this candle. I am open to any ideas you might have for the design but so far I have used a logo only on the jar which I really like BUT I still feel that it is not enough branding for people when you only show them the logo so I am considering adding the business name. Again, I am open to both ideas (with logo only or logo with business name (Silken Meadow).

IMPORTANT: YOU MAY IGNORE MY DESIGN COMPLETELY AND DO YOUR OWN ONE AS LONG AS YOU KERP THE LOGO DESIGN. YOU MAY ALSO ADJUST THE LOGO A BIT TO SUIT YOUR DESIGN. - sorry im using capital letters to show importance but im not yelling :)

UPDATE: To clarify, I have uploaded a video called Corvel in the box to show what the current product look like. It is a corvel jar with a logo only and the jar box has a window that shows the jar with the logo on it and the back of that jar box has a bigger version of the label that has more details (i.e. Fragrance name and website link). So to make it clear, I would like to have two versions of the lables: 1. on the jar with minimal info (logo only or logo with the business name) 2. Bigger version of the label with more info to put on the back of the jar box - as described above. The dimensions of the jars are as per this link https://www.lunaxo-example.com.au/corvel-medium-base-and-flat-lid-amber-packed-with-lid-on/ The dimensions of the jar box as per this link https://www.lunaxo-example.com.au/corvel-medium-flat-lid-candle-box-with-window-beige/ Looking forward to some artistic productions :)

Update #2: Tues 25 Dec 18 1. I have uploaded the photo which has the logo with the name 'Silken Meadow' below it just for a reference. However, I would like the designer to modify the current font and NOT to use it as the word 'of in the phrase 'Silken Meadow' does not come out clear enough after printing. 2. I would like the designer NOT to create a design that will require a clear sticker/label for printing. 3. I have attached the photos of my current designs on the jars or the jar box just as a reference but please do NOT just use the same fonts and only change background. I am hoping to see something different and more professional than my own design :) Thank you very much!

Font styles to use
Decorative
Script

Requirements
Must have
• I would like them to fit on the three colors of the jars below - white, amber and black. Below is a link to how the jar looks like https://www.lunaxo-example.com.au/candle-making-supplies/candle-jars/corvel-candle-jars/?glassware_colour=415,443,417&glassware_size=268
Nice to have
• I would like to have a modern design which is suitable for both feminine and musculine.
Should not have
• shouldnt have so much writing on it!

```html
<!DOCTYPE html>
<html lang="en">
<head>
<meta charset="utf-8">
<title>Silken Meadow — Jar Label and Gift Box</title>
<link href="https://fonts.googleapis.com/css2?family=Cinzel:wght@500&family=Archivo:wght@400;800&display=swap" rel="stylesheet">
<style>
  :root{
    --canvas:#ffffff;
    --box:#231f20;
    --label:#a89683;
    --label-light:#b7a693;
    --ink:#1b1718;
    --sticker:#c8b29a;
  }
  *{box-sizing:border-box;margin:0;padding:0}
  html,body{width:1200px;height:950px;overflow:hidden;background:var(--canvas)}
  .sheet{position:relative;width:1200px;height:950px}
  .brand{font-family:"Cinzel",serif;font-weight:500;color:var(--ink);line-height:1;text-align:left;letter-spacing:.02em}
  .body-text{font-family:"Archivo",sans-serif;color:var(--ink)}
  .label{position:absolute;background:var(--label);border-radius:6px;overflow:hidden;display:flex;align-items:center}
  .label-texture{position:absolute;inset:0;background:linear-gradient(135deg,var(--label-light),var(--label) 60%)}
  .label > *:not(.label-texture){position:relative}
  .rule{width:1px;background:var(--ink);align-self:stretch;margin:8px 0}
  .vertical{writing-mode:vertical-rl;transform:rotate(180deg)}

  /* jar label, full */
  .jar-label{left:245px;top:320px;width:256px;height:66px;padding:0 8px 0 14px;gap:9px}
  .jar-label .brand{font-size:18px;width:116px}
  .jar-label .fragrance{font-family:"Archivo",sans-serif;font-size:11px;line-height:1.05;text-align:center}
  .jar-label .notes{font-size:5px;font-weight:800;line-height:1.3;text-align:center;height:50px}
  .jar-label .burn{font-size:5px;font-weight:800;line-height:1.3;text-align:center}

  /* small jar labels */
  .mini-label{top:152px;width:84px;height:36px;padding-left:9px;border-radius:2px}
  .mini-label .brand{font-size:10px}
  .mini-1{left:680px}.mini-2{left:817px}.mini-3{left:953px}

  /* box panels */
  .panel{position:absolute;background:var(--box)}
  .box-lid{left:662px;top:295px;width:237px;height:235px}
  .lid-band{position:absolute;left:0;top:77px;width:237px;height:76px;background:var(--label);display:flex;align-items:center;justify-content:center;overflow:hidden}
  .lid-band .brand{position:relative;font-size:22px}

  .box-back{left:81px;top:640px;width:237px;height:235px}
  .back-sticker{position:absolute;left:60px;top:167px;width:114px;height:40px;background:var(--sticker);border-radius:5px;padding:5px 7px;text-align:center}
  .back-sticker h3{font-family:"Archivo",sans-serif;font-weight:400;font-size:6px;border-bottom:1px solid var(--ink);padding-bottom:3px;margin-bottom:3px}
  .back-sticker p{font-size:4.5px;font-weight:800;line-height:1.4}

  .box-side,.box-front{top:548px;width:238px;height:326px}
  .side-story{left:398px}
  .box-front{left:659px}
  .side-care{left:919px}
  .ribbon{position:absolute;top:0;width:77px;height:204px;background:var(--label);overflow:hidden;display:flex;justify-content:center;padding:10px 6px}
  .side-story .ribbon{left:76px;clip-path:polygon(0 0,100% 0,100% 86%,0 100%)}
  .side-care .ribbon{left:79px;clip-path:polygon(0 0,100% 0,100% 100%,0 89%)}
  .ribbon .copy{position:relative;writing-mode:vertical-rl;font-size:6px;font-weight:800;font-style:italic;line-height:1.45;max-height:160px}
  .ribbon .title{font-family:"Archivo",sans-serif;font-weight:400;font-style:normal;font-size:10px;letter-spacing:.12em;margin-left:4px}
  .ribbon .site{font-style:normal;font-weight:400;font-size:7px;margin-right:6px}

  .window{position:absolute;left:45px;top:48px;width:148px;height:230px;background:linear-gradient(90deg,#1a1a1a,#2b2b2b 45%,#151515);border-radius:3px}
  .window-label{left:10px;top:142px;width:138px;height:66px;padding-left:14px;border-radius:4px 0 0 4px}
  .window-label .brand{font-size:18px}
</style>
</head>
<body>
<main class="sheet">

  <section class="label jar-label" aria-label="Jar label">
    <div class="label-texture" role="img" aria-label="Soft flame-leaf pattern on taupe label"></div>
    <p class="brand">Silken<br>Meadow</p>
    <span class="rule"></span>
    <p class="fragrance vertical">TURKISH<br>ROSE</p>
    <p class="body-text notes vertical">Rose petals &amp; geranium<br>with lemon, clove &amp; lily<br>of the valley</p>
    <span class="rule"></span>
    <p class="body-text burn vertical">BURN TIME<br>40 Hours</p>
  </section>

  <div class="label mini-label mini-1"><div class="label-texture" role="img" aria-label="Label pattern"></div><p class="brand">Silken<br>Meadow</p></div>
  <div class="label mini-label mini-2"><div class="label-texture" role="img" aria-label="Label pattern"></div><p class="brand">Silken<br>Meadow</p></div>
  <div class="label mini-label mini-3"><div class="label-texture" role="img" aria-label="Label pattern"></div><p class="brand">Silken<br>Meadow</p></div>

  <section class="panel box-lid" aria-label="Gift box lid">
    <div class="lid-band">
      <div class="label-texture" role="img" aria-label="Flame-leaf pattern band"></div>
      <p class="brand">Silken<br>Meadow</p>
    </div>
  </section>

  <section class="panel box-back" aria-label="Gift box back">
    <div class="back-sticker">
      <h3>TURKISH ROSE</h3>
      <p class="body-text">WARNING: Never leave a burning candle unattended, keep away from children.</p>
    </div>
  </section>

  <section class="panel box-side side-story" aria-label="Gift box side">
    <div class="ribbon">
      <div class="label-texture" role="img" aria-label="Flame-leaf pattern ribbon"></div>
      <p class="body-text copy">Silken Meadow Candles are made to be like its name making the host (candle lover) keen to have our candles as a very welcomed guest anywhere, everywhere and always leaving a great experience behind after it has melted.</p>
    </div>
  </section>

  <section class="panel box-front" aria-label="Gift box front with window">
    <div class="window">
      <div class="label window-label">
        <div class="label-texture" role="img" aria-label="Label pattern"></div>
        <p class="brand">Silken<br>Meadow</p>
      </div>
    </div>
  </section>

  <section class="panel box-side side-care" aria-label="Gift box side">
    <div class="ribbon">
      <div class="label-texture" role="img" aria-label="Flame-leaf pattern ribbon"></div>
      <p class="body-text copy"><span class="title">LUXURY CANDLES</span>Our candles are made from natural soy wax, our candle wicks are made from cotton with no lead in it.<span class="site">silkenmeadow.com.au</span></p>
    </div>
  </section>

</main>
</body>
</html>
```